Boutique Financial Services/Advisor Business Needs Web Design

Looking for an informational and functional web design for my Financial Services/Financial Advisement business. It should have functionality for Company name, address, phone #, "About Us", Who we are, Our Mission, Services we offer, Biographies/Photos of/about "The Team", and possibly a link to "Contact Us". Would like to see something new & exciting blended with a traditional/professional look that will appeal to those approaching retirement, as well as those younger clients that are beginning to think about planning for the future. I already have a web domain through Brixwell, but would like this to be the design we use for that domain.
Financial Services/Financial Advisor
Coded - Design and coding required
1 page

```html
<!DOCTYPE html>
<html lang="en">
<head>
<meta charset="utf-8">
<title>Summitline Wealth Management</title>
<link rel="stylesheet" href="https://fonts.googleapis.com/css2?family=Cinzel:wght@400;500&family=Poppins:wght@300;400&display=swap">
<style>
:root{
  --navy:#0d0c4a;
  --indigo:#3a3c7c;
  --indigo-dark:#24266a;
  --ink:#222;
  --text:#555;
  --muted:#666;
  --light:#f4f4f4;
  --white:#fff;
}
*{margin:0;padding:0;box-sizing:border-box}
html,body{width:1200px;height:3077px;overflow:hidden;background:var(--white)}
body{position:relative;font-family:'Poppins',sans-serif;color:var(--text)}
.abs{position:absolute}
.serif{font-family:'Cinzel',serif;font-weight:400}

/* header */
.site-header{position:absolute;left:0;top:0;width:1200px;height:119px;background:var(--white)}
.brand{position:absolute;left:83px;top:44px;width:170px;font-family:'Poppins',sans-serif;font-weight:400;font-size:13px;letter-spacing:1px;color:var(--navy);line-height:1.4;display:flex;align-items:center;gap:8px}
.brand-dot{width:12px;height:12px;border-radius:50%;background:var(--navy);flex:none}
.main-nav{position:absolute;top:53px;left:650px;display:flex;gap:32px;font-size:13.5px;color:#444}
.nav-active{position:absolute;left:642px;top:0;width:59px;height:4px;background:var(--navy)}

/* hero */
.hero-media{position:absolute;left:0;top:119px;width:1200px;height:606px;background:radial-gradient(ellipse at 60% 60%,#a97b58 0%,#8f7b6c 18%,#b4b2b3 45%,#a9a8a9 100%)}
.hero-bump{position:absolute;left:520px;top:682px;width:162px;height:80px;background:var(--white);border-radius:81px 81px 0 0}
.hero-eyebrow{left:83px;top:204px;font-size:14px;letter-spacing:5px;color:var(--white);font-weight:300}
.hero-title{left:83px;top:224px;font-size:80px;line-height:92px;color:var(--white);letter-spacing:1px}
.hero-copy{left:91px;top:320px;width:420px;font-size:13.5px;line-height:25px;color:var(--white);font-weight:300}
.round-btn{position:absolute;width:46px;height:46px;border-radius:50%;display:flex;align-items:center;justify-content:center}
.round-btn.solid{background:var(--navy)}
.round-btn.ghost{border:1.5px solid var(--white)}

/* who we are */
.who-frame{left:91px;top:862px;width:439px;height:391px;background:var(--navy);border-radius:0 150px 0 90px}
.who-photo{left:115px;top:883px;width:416px;height:370px;background:linear-gradient(135deg,#dfe4e6,#b9c4c9 45%,#39547a 60%,#c9d2d6);border-radius:0 110px 0 90px}
.who-title{left:602px;top:925px;font-size:46px;color:var(--navy)}
.who-copy{left:602px;top:1000px;width:420px;font-size:13.5px;line-height:25px;color:var(--text)}
.outline-btn{left:602px;top:1212px;width:148px;height:42px;border:1.5px solid var(--navy);border-radius:21px;font-size:13.5px;color:var(--navy);display:flex;align-items:center;justify-content:center}

/* services */
.services-band{left:0;top:1418px;width:1200px;height:342px;background:linear-gradient(90deg,var(--indigo) 0%,var(--indigo) 55%,#2a2d74 75%,#1b1e62 100%);border-radius:0 120px 0 120px;overflow:hidden}
.services-title{left:116px;top:1482px;font-size:46px;color:var(--white)}
.services-sub{left:115px;top:1543px;font-size:14px;color:var(--white)}
.service-card{position:absolute;top:1615px;width:306px;height:271px;background:var(--white);border-radius:70px 0 0 60px;box-shadow:0 10px 30px rgba(0,0,0,.08);text-align:center}
.service-card svg.icon{margin-top:48px}
.service-card h3{font-family:'Cinzel',serif;font-weight:400;font-size:21px;color:var(--navy);margin-top:14px}
.service-card p{font-size:13.5px;line-height:25px;color:var(--text);margin:22px auto 0;width:220px}
.service-card .go{margin-top:14px}

/* team */
.team-title{left:0;top:1990px;width:1200px;text-align:center;font-size:46px;color:var(--navy)}
.member{position:absolute;top:2102px;width:230px}
.member-photo{width:230px;height:250px;border-radius:40px 40px 0 40px}
.member h4{font-family:'Cinzel',serif;font-weight:400;font-size:23px;color:var(--navy);margin:20px 0 0 18px}
.member p{font-size:13.5px;color:var(--text);margin:8px 0 0 18px}
.connect{position:absolute;left:0;top:0;width:230px;height:250px;border-radius:40px 40px 0 40px;background:rgba(58,60,124,.88);display:flex;flex-direction:column;align-items:center;justify-content:center;color:var(--white)}
.connect span{font-size:11px;letter-spacing:5px;margin-top:-10px}
.connect .socials{display:flex;gap:8px;margin-top:14px}
.connect .socials i{width:18px;height:18px;border-radius:50%;background:var(--white);display:block}

/* footer */
.site-footer{left:0;top:2553px;width:1200px;height:402px;background:var(--light);border-radius:110px 0 110px 0}
.footer-brand{left:135px;top:2700px;font-size:14px;letter-spacing:1px;color:var(--navy);display:flex;align-items:center;gap:8px}
.footer-col{position:absolute;top:2648px}
.footer-col h5{font-family:'Cinzel',serif;font-weight:400;font-size:21px;color:var(--navy);margin-bottom:22px}
.footer-col ul{list-style:none;font-size:13.5px;color:var(--text)}
.footer-col li{height:38px}
.contact-row{display:flex;gap:12px;font-size:13.5px;line-height:25px;color:var(--text)}
.copyright{left:0;top:3003px;width:1200px;text-align:center;font-size:13.5px;color:var(--text)}
</style>
</head>
<body>

<header class="site-header">
  <div class="brand"><span class="brand-dot"></span>SUMMITLINE WEALTH MANAGEMENT</div>
  <span class="nav-active"></span>
  <nav class="main-nav"><span>Home</span><span>About Us</span><span>Services we offer</span><span>Our Team</span><span>Contact Us</span></nav>
</header>

<section class="hero">
  <div class="hero-media" role="img" aria-label="Stacks of copper coins with rising white arrows and an upward trend line"></div>
  <div class="hero-bump"></div>
  <p class="abs hero-eyebrow">Your Success, Our Priority</p>
  <h1 class="abs serif hero-title">Financial</h1>
  <p class="abs hero-copy">Financial services include dummy text of the printing and typesetting industry. Lorem Ipsum has</p>
  <a class="round-btn solid" style="left:554px;top:702px" aria-label="Previous"><svg width="18" height="10" viewBox="0 0 18 10"><path d="M17 5H1M5 1L1 5l4 4" stroke="#fff" stroke-width="1.5" fill="none"/></svg></a>
  <a class="round-btn solid" style="left:601px;top:702px" aria-label="Next"><svg width="18" height="10" viewBox="0 0 18 10"><path d="M1 5h16M13 1l4 4-4 4" stroke="#fff" stroke-width="1.5" fill="none"/></svg></a>
</section>

<section class="who">
  <div class="abs who-frame"></div>
  <div class="abs who-photo" role="img" aria-label="Smiling advisor with arms crossed in front of a glass office building"></div>
  <h2 class="abs serif who-title">Who We Are</h2>
  <p class="abs who-copy">Financial services include dummy text of the printing and typesetting industry. Lorem Ipsum has been the industry's standard dummy text ever since the 1500s, when an unknown printer took a galley of type and scrambled it to make a type specimen book. It has survived not only five centuries, but also the leap into electronic typesetting, remaining essentially unchanged.</p>
  <a class="abs outline-btn">Learn More</a>
</section>

<section class="services">
  <div class="abs services-band" role="img" aria-label="Blue-tinted glass skyscraper facade"></div>
  <h2 class="abs serif services-title">Services We Offer</h2>
  <p class="abs services-sub">Consumer finance dummy text of the printing</p>
  <a class="round-btn ghost" style="left:998px;top:1507px" aria-label="Previous"><svg width="18" height="10" viewBox="0 0 18 10"><path d="M17 5H1M5 1L1 5l4 4" stroke="#fff" stroke-width="1.5" fill="none"/></svg></a>
  <a class="round-btn ghost" style="left:1047px;top:1507px" aria-label="Next"><svg width="18" height="10" viewBox="0 0 18 10"><path d="M1 5h16M13 1l4 4-4 4" stroke="#fff" stroke-width="1.5" fill="none"/></svg></a>

  <article class="service-card" style="left:115px">
    <svg class="icon" width="28" height="34" viewBox="0 0 28 34" fill="none" stroke="#0d0c4a" stroke-width="1.5"><rect x="1" y="1" width="26" height="32" rx="2"/><rect x="6" y="6" width="16" height="7"/><circle cx="8" cy="19" r=".8"/><circle cx="14" cy="19" r=".8"/><circle cx="20" cy="19" r=".8"/><circle cx="8" cy="25" r=".8"/><circle cx="14" cy="25" r=".8"/><circle cx="20" cy="25" r=".8"/></svg>
    <h3>Retirement Plan</h3>
    <p>Securities are simply dummy text of the printing</p>
    <svg class="go" width="18" height="10" viewBox="0 0 18 10"><path d="M1 5h16M13 1l4 4-4 4" stroke="#0d0c4a" stroke-width="1.3" fill="none"/></svg>
  </article>
  <article class="service-card" style="left:450px">
    <svg class="icon" width="40" height="30" viewBox="0 0 40 30" fill="none" stroke="#0d0c4a" stroke-width="1.5"><ellipse cx="15" cy="7" rx="13" ry="5"/><path d="M2 7v6c0 3 6 5 13 5"/><ellipse cx="25" cy="17" rx="13" ry="5"/><path d="M12 17v6c0 3 6 5 13 5s13-2 13-5v-6"/></svg>
    <h3>Foresight</h3>
    <p>Process of thinking is simply dummy text of the</p>
    <svg class="go" width="18" height="10" viewBox="0 0 18 10"><path d="M1 5h16M13 1l4 4-4 4" stroke="#0d0c4a" stroke-width="1.3" fill="none"/></svg>
  </article>
  <article class="service-card" style="left:784px">
    <svg class="icon" width="36" height="28" viewBox="0 0 36 28" fill="none" stroke="#0d0c4a" stroke-width="1.5"><rect x="1" y="1" width="34" height="26" rx="2"/><path d="M1 9h34M20 20h5M28 20h3"/></svg>
    <h3>Asset Management</h3>
    <p>Balancing of costs dummy text of the printing</p>
    <svg class="go" width="18" height="10" viewBox="0 0 18 10"><path d="M1 5h16M13 1l4 4-4 4" stroke="#0d0c4a" stroke-width="1.3" fill="none"/></svg>
  </article>
</section>

<section class="team">
  <h2 class="abs serif team-title">Meet Our Team</h2>
  <div class="member" style="left:115px">
    <div class="member-photo" role="img" aria-label="Portrait of Everett in a light grey blazer" style="background:linear-gradient(160deg,#cfd6d8,#a6a39f 55%,#d9d6d0)"></div>
    <h4>Everett</h4><p>Financial Planner</p>
  </div>
  <div class="member" style="left:363px">
    <div class="member-photo" role="img" aria-label="Portrait of Maren in a grey blazer" style="background:linear-gradient(160deg,#b9b9bd,#6b6a70)"></div>
    <div class="connect"><span>CONNECT</span><div class="socials"><i></i><i></i></div></div>
    <h4>Maren</h4><p>Certified Public Accountant</p>
  </div>
  <div class="member" style="left:611px">
    <div class="member-photo" role="img" aria-label="Portrait of Colin in a dark suit on a phone call" style="background:linear-gradient(160deg,#8e9092,#3b3c3e 60%,#6d6f71)"></div>
    <h4>Colin</h4><p>Budget Analyst</p>
  </div>
  <div class="member" style="left:859px">
    <div class="member-photo" role="img" aria-label="Portrait of Juliet in a black top in a bright office" style="background:linear-gradient(160deg,#e3e6e8,#c9b9ae 50%,#2b2b2d 85%)"></div>
    <h4>Juliet</h4><p>Portfolio Manager</p>
  </div>
</section>

<footer>
  <div class="abs site-footer"></div>
  <div class="abs footer-brand"><span class="brand-dot"></span>SUMMITLINE WEALTH<br>MANAGEMENT</div>
  <div class="footer-col" style="left:387px">
    <h5>Useful Links</h5>
    <ul><li>Home</li><li>About Us</li><li>Services We Offer</li><li>Meet Our Team</li></ul>
  </div>
  <div class="footer-col" style="left:633px">
    <h5>Resources</h5>
    <ul><li>Privacy Policy</li><li>Terms &amp; Conditions</li><li>Contact Us</li></ul>
  </div>
  <div class="footer-col" style="left:863px">
    <h5>Contact Details</h5>
    <div class="contact-row"><svg width="16" height="18" viewBox="0 0 16 18" fill="none" stroke="#777" stroke-width="1.2" style="margin-top:4px"><path d="M8 17s6-6 6-10A6 6 0 0 0 2 7c0 4 6 10 6 10z"/><circle cx="8" cy="7" r="2"/></svg><span>Nora Whitfield<br>218 Harbor Ln.<br>Clear Lake, TX 77058</span></div>
    <div class="contact-row" style="margin-top:24px"><svg width="16" height="16" viewBox="0 0 16 16" fill="none" stroke="#777" stroke-width="1.2" style="margin-top:4px"><path d="M3 1l3 3-2 2c1 2 4 5 6 6l2-2 3 3-2 2C8 15 1 8 1 3z"/></svg><span>+1-555-014-2210</span></div>
    <div class="contact-row"><svg width="16" height="14" viewBox="0 0 16 14" fill="none" stroke="#777" stroke-width="1.2" style="margin-top:5px"><rect x="1" y="1" width="14" height="12" rx="1"/><path d="M1 2l7 6 7-6"/></svg><span>hello@summitline.example</span></div>
  </div>
  <p class="abs copyright">© 2024 Summitline Wealth Management. All rights reserved.</p>
</footer>

</body>
</html>
```